RK Tannery Construction Inc.

Design a new business card for our construction company
To be removed from current card:
Delete 25 years
Delete Tenant fit up Renovations section

```html
<!DOCTYPE html>
<html lang="en">
<head>
<meta charset="utf-8">
<title>RK Tannery Construction Inc. – Business Card</title>
<link href="https://fonts.googleapis.com/css2?family=Krona+One&family=Exo+2:wght@400;500&display=swap" rel="stylesheet">
<style>
  :root {
    --purple: #552d75;
    --teal: #23786c;
    --slate: #3c4f70;
    --white: #ffffff;
    --ink: #2d2d2d;
    --backdrop: #c4c4c4;
  }
  * { box-sizing: border-box; margin: 0; padding: 0; }
  html, body { width: 1200px; height: 800px; overflow: hidden; }
  body {
    background: var(--backdrop);
    display: flex;
    align-items: center;
    justify-content: center;
    gap: 40px;
    font-family: "Exo 2", sans-serif;
  }
  .card {
    position: relative;
    width: 540px;
    height: 309px;
    border-radius: 18px;
    overflow: hidden;
    box-shadow: 0 8px 24px rgba(0,0,0,.18);
  }

  /* Front */
  .card-front { background: var(--white); }
  .accent-square {
    position: absolute;
    top: 0; right: 64px;
    width: 86px; height: 62px;
    background: var(--purple);
  }
  .holder-name {
    position: absolute;
    left: 34px; top: 48px;
    font-family: "Krona One", sans-serif;
    font-size: 15px;
    letter-spacing: .5px;
    color: var(--purple);
  }
  .holder-name .surname { color: var(--teal); }
  .contact-band {
    position: absolute;
    left: 0; top: 126px;
    width: 292px; height: 98px;
    background: var(--teal);
    padding: 12px 0 0 30px;
    list-style: none;
    color: var(--white);
    font-size: 13.5px;
    line-height: 20px;
  }
  .contact-band li { display: flex; align-items: center; gap: 8px; }
  .contact-band svg { width: 12px; height: 12px; flex: none; }
  .address {
    position: absolute;
    left: 30px; top: 238px;
    color: var(--ink);
    font-size: 14px;
    line-height: 19px;
  }
  .wordmark-front {
    position: absolute;
    left: 316px; top: 120px;
    font-family: "Krona One", sans-serif;
    color: var(--teal);
    line-height: 1.25;
  }
  .wordmark-front .main { font-size: 22px; }
  .wordmark-front .sub { font-size: 11.5px; letter-spacing: 1.6px; }

  /* Back */
  .card-back {
    background: linear-gradient(35deg, var(--purple) 0%, var(--slate) 45%, var(--teal) 85%);
    color: var(--white);
    font-family: "Krona One", sans-serif;
  }
  .wordmark-back {
    position: absolute;
    left: 68px; top: 96px;
    line-height: 1.25;
  }
  .wordmark-back .main { font-size: 38px; }
  .wordmark-back .sub { font-size: 18.5px; letter-spacing: 2.4px; }
  .sectors {
    position: absolute;
    left: 68px; bottom: 52px;
    font-size: 12px;
    letter-spacing: .5px;
  }
</style>
</head>
<body>
  <section class="card card-front">
    <div class="accent-square"></div>
    <h1 class="holder-name">MARC <span class="surname">TANNERY</span></h1>
    <ul class="contact-band">
      <li><svg viewBox="0 0 12 12"><path d="M3 1l2 2.2-1.2 1.3a6 6 0 003.7 3.7L8.8 7 11 9l-1.4 2C5 11 1 7 1 2.4z" fill="currentColor"/></svg>613-555-0142 ext.221</li>
      <li><svg viewBox="0 0 12 12"><rect x="3" y=".8" width="6" height="10.4" rx="1" fill="none" stroke="currentColor" stroke-width="1.3"/><circle cx="6" cy="9.4" r=".7" fill="currentColor"/></svg>613-555-0187</li>
      <li><svg viewBox="0 0 12 12"><rect x=".8" y="2.3" width="10.4" height="7.4" fill="none" stroke="currentColor" stroke-width="1.3"/><path d="M.8 2.3L6 6.6l5.2-4.3" fill="none" stroke="currentColor" stroke-width="1.3"/></svg>marc@rktanneryconst.ca</li>
      <li><svg viewBox="0 0 12 12" fill="none" stroke="currentColor" stroke-width="1.1"><circle cx="6" cy="6" r="5"/><ellipse cx="6" cy="6" rx="2.2" ry="5"/><path d="M1 6h10M1.8 3.5h8.4M1.8 8.5h8.4"/></svg>www.rktanneryconstruction.ca</li>
    </ul>
    <p class="address">1280 Meadowbrook Rd., Suite 100<br>Ottawa, On K1A 0B1</p>
    <div class="wordmark-front">
      <div class="main">RK TANNERY</div>
      <div class="sub">CONSTRUCTION INC.</div>
    </div>
  </section>

  <section class="card card-back">
    <div class="wordmark-back">
      <div class="main">RK TANNERY</div>
      <div class="sub">CONSTRUCTION INC.</div>
    </div>
    <p class="sectors">OFFICE | RETAIL | INSTITUTIONAL</p>
  </section>
</body>
</html>
```